Ferlane Capital, a private equity fund, needs a brochure

Ferlane Capital is a private equity fund dedicated to the development of budget hotels in France (reasonably priced hotel rooms).
Our customers are French private and high-income investors.

The brochure should communicate :
- seriousness and expertise
- trust, confidence and security
- financial product and profitability

The title is : Investissez dans l'hôtellerie économique et l'immobilier

Brochure size :
3 pages A4
Open size : 63 x 29,7 cm
Closed size : 21 x 29,7 cm

Our competitors :
Brivento http://brivento-immo-example.fr/
789 Ventara http://www.789ventara-example.com/
LMR Capital http://www.lmrex-example.com/
Solvio capital http://www.solviocapital-example.fr/
Dravomont http://www.dravomont-example.fr/

Target Market(s)

Private investors, high-income ; Institutional investors ; Target customers are French private investors with high revenue.

Industry/Entity Type

Financial

Requirements
Must have
• - Brochure must respect our identity (you can see our logo) and use its colors and typo (and/or same typo style)
- You must use pictures on each interior pages (pictures of projetc and hotels)

```html
<!DOCTYPE html>
<html lang="fr">
<head>
<meta charset="utf-8">
<title>Ferlane Capital – Brochure intérieure</title>
<link href="https://fonts.googleapis.com/css2?family=Cormorant+SC:wght@500;600&family=Open+Sans:wght@400;600&display=swap" rel="stylesheet">
<style>
:root{
  --red:#8c1c1c;
  --red-dark:#6e1212;
  --brown:#5a3a2c;
  --brown-light:#a88470;
  --ink:#2a2a2a;
  --grey-box:#e4e1de;
  --strip:#e9e7e5;
  --paper:#ffffff;
}
*{margin:0;padding:0;box-sizing:border-box}
html,body{width:1200px;height:566px;overflow:hidden;background:var(--paper)}
.spread{position:relative;width:1200px;height:566px;font-family:"Open Sans",Arial,sans-serif;color:var(--ink);font-size:4.6px;line-height:1.5}
.spread p{margin-bottom:4px}
.col{position:absolute}
.heading{font-family:"Cormorant SC",Georgia,serif;font-weight:600;color:var(--red);font-size:15.5px;line-height:1;margin-bottom:14px;letter-spacing:.2px}
.callout{font-family:"Cormorant SC",Georgia,serif;color:var(--red);font-size:7.2px;line-height:1.25;border-left:1px solid var(--red);padding:3px 0 3px 5px;margin:8px 0}
.facts{list-style:none;margin:6px 0 10px}
.facts li{color:var(--red);border-left:1px solid var(--red);padding:2px 0 2px 5px;margin-bottom:6px}
.grey-box{position:absolute;background:var(--grey-box)}
.quote-box{position:absolute;left:33px;top:290px;width:88px;height:56px;background:var(--grey-box);padding:8px 6px;font-family:"Cormorant SC",Georgia,serif;color:var(--red);font-size:7px;line-height:1.15;text-align:center}
.photo{position:absolute}
.strip{position:absolute;left:0;top:447px;width:1200px;height:119px;background:var(--strip)}
.fold{position:absolute;top:0;width:1px;height:566px;background:#eeeceb}
.chart-bar{position:absolute;left:848px;top:266px;width:340px;height:14px;background:#efedeb;color:var(--red);font-size:5px;font-weight:600;text-align:center;line-height:14px}
.chart{position:absolute;left:840px;top:285px}
.chart-note{position:absolute;left:1106px;top:300px;width:82px;font-size:4.4px}
</style>
</head>
<body>
<div class="spread">
  <div class="fold" style="left:400px"></div>
  <div class="fold" style="left:820px"></div>

  <!-- Panel 1 -->
  <section class="col" style="left:33px;top:28px;width:168px">
    <h2 class="heading">Un véhicule<br>innovant</h2>
    <p style="margin-top:22px">FERLANE CAPITAL (Hôtels Bon Séjour) est une société d'investissement constituée sous la forme d'une SAS à capital variable ayant opté pour le régime fiscal des sociétés de capital-risque (« SCR »).</p>
    <p class="callout">Les Sociétés de capital-risque bénéficient d'un régime fiscal de faveur prévu par la Loi n° 85-695 du 11 juillet 1985 et les dispositions légales et réglementaires du Code général des impôts.</p>
    <p>Les associés personnes physiques peuvent bénéficier d'un régime d'exonération d'impôt sur le revenu pour les dividendes perçus et les plus-values de cession de titres réalisées (seules les contributions sociales restent applicables) à condition notamment de conserver les actions et de réinvestir leurs produits dans la SCR pendant une durée de 5 ans.</p>
    <p>Les conditions d'application de ce régime sont présentées à titre indicatif et de manière synthétique dans un document annexe auquel il convient de se reporter.</p>
  </section>
  <div class="quote-box">« Nous nous positionnons sur des marchés en croissance qui ont prouvé leur résistance face à la crise. »</div>
  <div class="photo" role="img" aria-label="Portrait du dirigeant" style="left:121px;top:318px;width:75px;height:82px;background:linear-gradient(160deg,#cfc6bd,#8a7868)"></div>

  <section class="col" style="left:222px;top:28px;width:170px">
    <h2 class="heading">Une société de capital-risque conçue et gérée par le Groupe Norval Outremer</h2>
    <p>Fort d'une connaissance approfondie en ingénierie financière et en promotion immobilière, le Groupe NORVAL OUTREMER et ses filiales bénéficient d'une expérience de plus de vingt ans dans la structuration financière, juridique et fiscale d'investissements immobiliers et industriels.</p>
    <ul class="facts">
      <li>4000 projets structurés et financés depuis vingt ans.</li>
      <li>3000 investisseurs satisfaits.</li>
      <li>800 sociétés sous gestion.</li>
    </ul>
    <h2 class="heading" style="margin-top:14px">Des investissements centrés sur l'hôtellerie et l'immobilier</h2>
    <p>FERLANE CAPITAL a pour objectif d'accueillir jusqu'à 30 millions d'euro de souscriptions sur 2 ans. Le produit de ces souscriptions permettra la prise de participations minoritaires (40% maximum) dans le capital de sociétés ayant pour objet :</p>
    <ul class="facts">
      <li>La construction ou l'acquisition d'hôtels économiques et leur exploitation.</li>
      <li>La construction ou l'acquisition de meublés de tourisme et leur exploitation.</li>
      <li>La construction-vente d'immeuble en VEFA.</li>
    </ul>
    <p>L'activité d'FERLANE CAPITAL est notamment centrée sur l'investissement dans des sociétés développant une activité commerciale d'exploitation d'hôtels économiques. Ces sociétés du portefeuille seront à terme propriétaires des actifs immobiliers qu'elles exploitent.</p>
    <p>FERLANE CAPITAL pourra également diversifier ses investissements dans les secteurs de la promotion immobilière et de l'immobilier de service (meublés de tourisme et/ou résidences médicalisées).</p>
  </section>

  <!-- Panel 2 -->
  <div class="grey-box" style="left:428px;top:18px;width:188px;height:238px"></div>
  <section class="col" style="left:437px;top:28px;width:172px">
    <h2 class="heading" style="text-align:center">Pourquoi l'hôtellerie<br>et l'immobilier ?</h2>
    <p>Dans des conditions économiques et financières perturbées depuis la crise financière de 2008, les investisseurs exigent aujourd'hui des placements structurés pour résister aux effets économiques induits. Selon l'analyse des équipes de Ferlane Capital, le marché de l'hôtellerie économique en croissance dispose d'une situation répond particulièrement bien à ces attentes. Ce positionnement est en adéquation avec la baisse des budgets alloués aux déplacements et voyages professionnels et touristiques.</p>
    <p>Le marché de l'immobilier reste quant à lui une valeur refuge en temps de crise, selon l'analyse des équipes de Ferlane Capital.</p>
    <ul class="facts">
      <li>Un marché en croissance malgré la crise.</li>
      <li>Sur 2011, la croissance cumulée du nombre de nuitées atteint + 3,2% par rapport à 2010. (source VERIDEX)</li>
      <li>Secteur porteur, 1,5 milliard d'euros ont été investis dans le secteur de l'hôtellerie en France en 2011. (source VERIDEX)</li>
    </ul>
  </section>
  <section class="col" style="left:437px;top:268px;width:172px">
    <h2 class="heading">Un partenariat avec Orsay Hotels Group</h2>
    <p>Pour l'exploitation des investissements hôteliers, les sociétés du portefeuille interviendront en partenariat avec un opérateur hôtelier — ORSAY HOTELS GROUP — dans le cadre d'un accord de franchise (Orsay Hotels Group, 2ème opérateur d'Europe, plus de 1000 hôtels dans le monde).</p>
    <ul class="facts">
      <li>Contrats de franchise sous enseignes : Escale Classe **, Clairval *** et Lilas Inn ***.</li>
      <li>Contrats d'assistance technique.</li>
      <li>Implantation de plus de 12 hôtels dans 6 régions françaises d'outremer.</li>
    </ul>
  </section>
  <section class="col" style="left:627px;top:28px;width:172px">
    <h2 class="heading">Focus sur l'hôtellerie économique dans les régions françaises ultramarines</h2>
    <p>Le marché des hôtels économiques normés et standardisés sous enseigne nationale ou internationale est peu développé dans les DOM-COM. Ces régions sont équipées principalement d'hôtels balnéaires à vocation touristique essentiellement implantés sur des lieux généralement éloignés des centres économiques. Depuis une vingtaine d'années, le développement important des populations et la centralisation des zones commerciales et industrielles sur les capitales administratives ont généré d'importants embouteillages qui compliquent les accès à ces zones. L'offre hôtelière n'est plus en adéquation avec les attentes des visiteurs professionnels. La création d'une chaîne d'hôtels économiques est la réponse à ce besoin et bénéficie de l'appui de la puissance publique et des instances régionales.</p>
    <ul class="facts">
      <li>Absence d'hôtels économiques standardisés et normés dans ces régions.</li>
      <li>Structures hôtelières existantes inadaptées aux besoins du marché professionnel et coûteuses : prix des nuitées proposées par ces nouveaux hôtels inférieurs de 30 à 50% aux prix pratiqués localement.</li>
      <li>Programmes d'investissements bénéficiant d'avantages fiscaux, sociaux et de subventions.</li>
    </ul>
  </section>
  <section class="col" style="left:627px;top:268px;width:172px">
    <h2 class="heading">Immobilier, valeur refuge pour l'investisseur (selon l'analyse d'Ferlane Capital)</h2>
    <ul class="facts">
      <li>Un investissement dans la pierre.</li>
      <li>Une réponse à l'incertitude des marchés financiers et de la monnaie et des risques d'inflation.</li>
      <li>Des emplacements exceptionnels (centres villes, aéroports, zones commerciales).</li>
    </ul>
  </section>

  <!-- Panel 3 -->
  <section class="col" style="left:848px;top:28px;width:180px">
    <h2 class="heading">Trois sources potentielles de gains :</h2>
    <p style="margin-top:8px">Une double plus-value potentielle hôtelière et immobilière assortie d'un rendement annuel. La création de valeur pour chacun des hôtels dans lesquels FERLANE CAPITAL prendra des participations provienda de la valorisation des murs de l'hôtel, de la valorisation de son fonds de commerce et de la rentabilité annuelle de l'exploitation. L'activité de location de meublés de tourisme bénéficie des mêmes synergies.</p>
    <p>La création de valeur pour l'activité de promotion immobilière (construction vente des immeubles) provienda des marges dégagées par les opérations de promotion</p>
    <ul class="facts">
      <li>Trois sources potentielles de gains, assorties toutefois d'un risque de perte en capital</li>
      <li>Atténuation de risques du fait de l'investissement diversifié dans les murs et dans le fonds de commerce</li>
      <li>Un recours à un financement peu coûteux</li>
    </ul>
  </section>
  <section class="col" style="left:1055px;top:28px;width:135px">
    <h2 class="heading">Comment sont répartis les gains ?</h2>
    <p style="margin-top:8px">Le capital de la société FERLANE CAPITAL est constitué de deux types de catégorie d'actions A et B.</p>
    <ul class="facts">
      <li>Les actions de type A destinées aux investisseurs.</li>
      <li>Les actions de type B (carried-interest) destinées à être souscrites par les personnes intervenant dans la gestion de FERLANE CAPITAL</li>
      <li>En vertu des dispositions légales et statutaires applicables, l'émission de 100 actions de type A oblige à émettre 1 action B. Ne peuvent être souscrite que par les personnes intervenant dans la gestion de FERLANE CAPITAL.</li>
    </ul>
    <p>Les droits préférentiels attachés aux actions A et aux actions B sont définis à l'article 14.2 des statuts de FERLANE CAPITAL et répondent notamment au principe selon lequel l'actif net de liquidation au-delà d'un "rendement" de 7% l'an sera réparti à hauteur de 80% pour les actions A (investisseurs) et 20% pour les actions B (personnes intervenant dans la gestion du fonds).</p>
  </section>

  <div class="chart-bar">Plus-values hôtelières.&nbsp; | &nbsp;Plus-values immobilières.&nbsp; | &nbsp;Rendement annuel capitalisé.</div>
  <svg class="chart" width="262" height="160" viewBox="0 0 262 160" aria-label="Schéma de répartition des gains">
    <defs>
      <linearGradient id="wedge" x1="0" x2="1" y1="0" y2="0">
        <stop offset="0" stop-color="#f3eeea"/><stop offset="1" stop-color="#d9cbc2"/>
      </linearGradient>
    </defs>
    <polygon points="78,112 160,20 160,112" fill="url(#wedge)"/>
    <line x1="78" y1="110" x2="155" y2="25" stroke="#333" stroke-width=".5" stroke-dasharray="2,1.5"/>
    <polygon points="155,25 151,26 154,29" fill="#333"/>
    <text x="122" y="68" font-size="4.6" fill="#8c1c1c" text-anchor="middle">Espérance de gains</text>
    <text x="122" y="74" font-size="4.6" fill="#8c1c1c" text-anchor="middle">pour l'investisseur</text>
    <rect x="8" y="113" width="68" height="20" fill="#8c1c1c"/>
    <text x="42" y="125" font-size="4.8" fill="#fff" text-anchor="middle">Investissements</text>
    <rect x="160" y="20" width="78" height="34" fill="#a88470"/>
    <text x="199" y="39" font-size="4.8" fill="#fff" text-anchor="middle">Plus-values hôtelières</text>
    <rect x="160" y="56" width="78" height="30" fill="#5a3a2c"/>
    <text x="199" y="73" font-size="4.8" fill="#fff" text-anchor="middle">Plus-values immobilières</text>
    <rect x="160" y="88" width="78" height="23" fill="#1c1c1c"/>
    <text x="199" y="98" font-size="4.6" fill="#fff" text-anchor="middle">Rendement annuel</text>
    <text x="199" y="104" font-size="4.6" fill="#fff" text-anchor="middle">capitalisé</text>
    <rect x="160" y="113" width="96" height="20" fill="#8c1c1c"/>
    <text x="208" y="122" font-size="4.6" fill="#fff" text-anchor="middle">Remboursement</text>
    <text x="208" y="128" font-size="4.6" fill="#fff" text-anchor="middle">du capital initial</text>
    <line x1="242" y1="20" x2="242" y2="111" stroke="#333" stroke-width=".4"/>
    <text transform="translate(249,66) rotate(-90)" font-size="4.2" fill="#333" text-anchor="middle">Bénéfices bruts</text>
    <line x1="8" y1="136" x2="180" y2="136" stroke="#333" stroke-width=".4"/>
    <g font-size="4.6" fill="#333" text-anchor="middle">
      <text x="14" y="143">2012</text><text x="36" y="143">2013</text><text x="58" y="143">2014</text>
      <text x="118" y="143">2017</text><text x="166" y="143">2019</text>
    </g>
    <line x1="166" y1="145" x2="166" y2="150" stroke="#8c1c1c" stroke-width=".5"/>
    <text x="166" y="154" font-size="4.4" fill="#8c1c1c" text-anchor="middle">Possibilité</text>
    <text x="166" y="159" font-size="4.4" fill="#8c1c1c" text-anchor="middle">de sortie</text>
  </svg>
  <p class="chart-note">L'attention des investisseurs est toutefois attirée sur l'impact de l'effet enseigne d'un tel affichage, lequel peut masquer de mauvais résultats pour certains fonds en particulier et lequel ne préjuge pas de performances d'un niveau équivalent pour le présent fond (étant entendu que le risque de perte en capital est présent). Par ailleurs, l'attention des investisseurs est attirée sur les facteurs de risques liés à un investissement dans Ferlane Capital présentés ci-après dans le présent document.</p>

  <!-- Photo strip -->
  <div class="strip"></div>
  <div class="photo" role="img" aria-label="Photo d'un immeuble d'hôtel moderne sous ciel bleu" style="left:35px;top:463px;width:165px;height:88px;background:linear-gradient(180deg,#6f9fd0 0%,#a9c8e6 45%,#c9c2b4 70%,#7f8c6a 100%)"></div>
  <div class="photo" role="img" aria-label="Photo d'un hôtel économique à façade orange" style="left:222px;top:463px;width:168px;height:88px;background:linear-gradient(180deg,#9fc2e4 0%,#d7a866 45%,#c47a3a 70%,#8b8679 100%)"></div>
  <div class="photo" role="img" aria-label="Perspective d'un projet hôtelier avec végétation" style="left:438px;top:462px;width:108px;height:62px;background:linear-gradient(180deg,#e7ebee,#8fa77a 60%,#5d7a4a)"></div>
  <div class="photo" role="img" aria-label="Perspective d'un ensemble résidentiel" style="left:550px;top:460px;width:106px;height:50px;background:linear-gradient(180deg,#dfe7ef,#b9b3a5 55%,#6f8a5a)"></div>
  <div class="photo" role="img" aria-label="Perspective d'un complexe hôtelier" style="left:661px;top:462px;width:130px;height:48px;background:linear-gradient(180deg,#e4eaf0,#c9c0ae 50%,#7c9262)"></div>
  <div class="photo" role="img" aria-label="Vue aérienne d'un projet en bord de route" style="left:616px;top:512px;width:110px;height:38px;background:linear-gradient(180deg,#d9e2e8,#9aa88a 50%,#6a7f56)"></div>
  <div class="photo" role="img" aria-label="Photo d'une chambre d'hôtel" style="left:848px;top:462px;width:78px;height:88px;background:linear-gradient(160deg,#c9a98a,#7a5a44 60%,#3e2c22)"></div>
  <div class="photo" role="img" aria-label="Photo d'une chambre d'hôtel lumineuse" style="left:931px;top:462px;width:118px;height:88px;background:linear-gradient(160deg,#e9e3da,#b9a893 60%,#8a745e)"></div>
  <div class="photo" role="img" aria-label="Photo d'une chambre d'hôtel aux tons verts" style="left:1055px;top:462px;width:132px;height:88px;background:linear-gradient(160deg,#dfe3cf,#a7b46a 55%,#6d5a46)"></div>
</div>
</body>
</html>
```